Thank You Card for Customer Purchase

I need a thank you card designed to go out with my product once a customer has purchased. It will require some content creation but only a couple of lines.

It needs be basically state something along the lines of

"Thank you for your purchase..........
as well as some sort of speal about the company as well as contact details"

I have attached our brand guide to assist you. I will also provide you the url so you may get an idea of the company and the way we talk.

The document should be double sided A5 In size Landscape and be print ready as well. Provided in illustrator and pdf files. I have attached a template that is to be used and there is a printing instructions PDF document you need to follow as well.

Please contact if you have any questions

Target Market(s)

Young people aroung 20-40 male and female. Cool people

Industry/Entity Type

Printing

Requirements
Must have
• be cool and inline with brand guideline. please check out www.brodymarsh.com.au for ideas.

```html
<!DOCTYPE html>
<html lang="en">
<head>
<meta charset="utf-8">
<title>Brody Marsh – Thank You Card</title>
<link href="https://fonts.googleapis.com/css2?family=Courier+Prime:wght@400;700&family=Questrial&display=swap" rel="stylesheet">
<style>
  :root {
    --stage: #efefed;
    --frame: #58585a;
    --paper: #ffffff;
    --ink: #555557;
    --ink-soft: #6a6a6c;
    --rule: #b9cfe0;
    --brand-green: #7cc36e;
    --brand-blue: #3aa0c8;
    --pill: #e3e3e3;
    --logo-tile: #e6e6e6;
  }
  * { margin: 0; padding: 0; box-sizing: border-box; }
  html, body { width: 1200px; height: 498px; overflow: hidden; background: var(--stage); }
  .canvas { position: relative; width: 1200px; height: 498px; }

  .card {
    position: absolute;
    width: 552px; height: 394px;
    border: 13px solid var(--frame);
    background: var(--paper);
    font-family: "Questrial", sans-serif;
    color: var(--ink);
  }
  .card--front { left: 30px; top: 36px; }
  .card--back { left: 616px; top: 70px; }

  /* Front */
  .brand-name {
    position: absolute; left: 17px; top: 112px; width: 186px;
    text-align: center; font-size: 19px; letter-spacing: 3px; color: var(--ink);
  }
  .brand-rule { position: absolute; left: 17px; top: 143px; width: 186px; height: 1px; background: var(--rule); }
  .frames-art {
    position: absolute; left: 13px; top: 159px; width: 176px; height: 192px;
    background: linear-gradient(160deg, #f3f3f3, #e4e4e4);
  }
  .burst-art {
    position: absolute; left: 221px; top: 7px; width: 296px; height: 304px;
    background: radial-gradient(circle at 50% 55%, rgba(124,195,110,.55) 0%, rgba(90,170,210,.4) 45%, rgba(255,255,255,0) 72%);
  }
  .thanks-badge { position: absolute; left: 285px; top: 113px; width: 156px; height: 156px; }
  .thanks-text {
    position: absolute; left: 285px; top: 143px; width: 156px;
    text-align: center; font-family: "Courier Prime", monospace; font-weight: 700;
    font-size: 35px; line-height: 43px; color: #fff;
  }
  .purchase-pill {
    position: absolute; left: 227px; top: 329px; width: 270px; height: 27px;
    border-radius: 14px; background: var(--pill);
    font-family: "Courier Prime", monospace; font-weight: 700; font-size: 22px;
    line-height: 27px; text-align: center; color: var(--ink); letter-spacing: 1px;
  }

  /* Back */
  .banner { position: absolute; left: 9px; top: 8px; width: 510px; height: 143px; background: var(--brand-green); }
  .specs-photo {
    position: absolute; left: 142px; top: 25px; width: 218px; height: 76px;
    background: linear-gradient(120deg, #3a2414, #7a4a22 45%, #2c1a0e);
    border-radius: 10px 10px 30px 30px;
  }
  .tagline {
    position: absolute; left: 0; top: 117px; width: 100%; text-align: center;
    font-family: "Courier Prime", monospace; font-size: 11px; letter-spacing: 1.5px; color: #fff;
  }
  .letter {
    position: absolute; left: 28px; top: 167px; width: 470px;
    font-size: 9.6px; line-height: 11.5px; color: var(--ink-soft);
  }
  .letter p { margin-bottom: 10px; }
  .letter .contact { color: var(--brand-blue); font-weight: 700; font-size: 11px; }
  .letter .sign-off { margin-bottom: 0; }
  .disclaimer {
    position: absolute; left: 28px; top: 345px; width: 300px;
    font-size: 7px; line-height: 9px; font-style: italic; color: var(--ink);
  }
  .logo-tile {
    position: absolute; left: 381px; top: 290px; width: 118px; height: 66px;
    background: var(--logo-tile); display: flex; align-items: center; justify-content: center;
    font-size: 10px; letter-spacing: 1.5px; color: var(--ink);
  }
</style>
</head>
<body>
<main class="canvas">

  <section class="card card--front" aria-label="Card front">
    <div class="brand-name">BRODY MARSH</div>
    <div class="brand-rule"></div>
    <div class="frames-art" role="img" aria-label="Light grey outline drawings of assorted eyeglass frames"></div>
    <div class="burst-art" role="img" aria-label="Burst of green, blue and grey geometric triangles"></div>
    <svg class="thanks-badge" viewBox="0 0 156 156" aria-hidden="true">
      <circle cx="78" cy="78" r="78" fill="#e6e6e6"/>
      <circle cx="78" cy="78" r="70" fill="#58585a"/>
      <circle cx="78" cy="78" r="64" fill="none" stroke="#ffffff" stroke-width="1.5"/>
    </svg>
    <div class="thanks-text">Thank<br>You</div>
    <div class="purchase-pill">For Your Purchase</div>
  </section>

  <section class="card card--back" aria-label="Card back">
    <div class="banner">
      <div class="specs-photo" role="img" aria-label="Photo of tortoiseshell eyeglasses"></div>
      <div class="tagline">ADDICTED TO BRODY.</div>
    </div>
    <div class="letter">
      <p>It is with great pleasure we present you with your new Brodys.</p>
      <p>We hope they are an absolute joy to wear.</p>
      <p>If you have any questions or concerns about your new specs please don’t hesitate to get in touch with us on<br>
        <span class="contact">1300 555 014</span> or <span class="contact">admin@brodymarsh.com.au</span>.</p>
      <p>If you were happy with our service and product we would love it if you can spread the word about us via Pagebook, Picstream or any other way you want to your friends, colleagues and family.</p>
      <p>Happy Seeing.</p>
      <p class="sign-off">Love.<br>Brody Marsh</p>
    </div>
    <p class="disclaimer">DISCLAIMER: Brodys are highly addictive. We cannot be held responsible for habits that are formed as a result of this purchase.</p>
    <div class="logo-tile">BRODY MARSH</div>
  </section>

</main>
</body>
</html>
```